Australian Software Consultancy needs new Business Card Design

Design Business Card based on existing design artefacts (attached). We are open to all designs. As its a 2 sided design and we thought it might be quite striking to have one side with a black background and te other side with a white background.

Target Market(s)

Financial Services mainly.

Industry/Entity Type

Business

Contact Information for Business Card

Name :
Position :
Email :

Requirements
Must have
• Funky design using our existing assets

```html
<!DOCTYPE html>
<html lang="en">
<head>
<meta charset="utf-8">
<title>Deep Logic Business Card</title>
<link href="https://fonts.googleapis.com/css2?family=Exo+2:wght@400;600;700;800&display=swap" rel="stylesheet">
<style>
  :root {
    --stage: #1c1c1c;
    --card-dark: #151515;
    --card-light: #ffffff;
    --ink: #111111;
    --accent: #e3232b;
    --white: #ffffff;
    --muted: #2a2a2a;
    --map-dot: #3a3a3a;
  }
  * { margin: 0; padding: 0; box-sizing: border-box; }
  html, body {
    width: 1200px;
    height: 1000px;
    overflow: hidden;
    background: var(--stage);
    font-family: "Exo 2", sans-serif;
  }
  .stage {
    position: relative;
    width: 1200px;
    height: 1000px;
  }
  .card {
    position: absolute;
    left: 300px;
    width: 600px;
    height: 342px;
    border-radius: 18px;
    overflow: hidden;
  }
  .card-front {
    top: 90px;
    background: var(--card-dark);
  }
  .card-back {
    top: 520px;
    background: var(--card-light);
  }
  .world-map-area {
    position: absolute;
    left: 70px;
    top: 40px;
    width: 470px;
    height: 270px;
    border-radius: 40px;
    background: radial-gradient(ellipse at center, var(--map-dot) 0%, var(--muted) 45%, rgba(21,21,21,0) 75%);
    opacity: 0.8;
  }
  .front-wordmark {
    position: absolute;
    left: 0;
    right: 0;
    top: 140px;
    text-align: center;
    font-weight: 800;
    font-size: 58px;
    letter-spacing: 2px;
    color: var(--white);
  }
  .back-wordmark {
    position: absolute;
    right: 40px;
    top: 50px;
    font-weight: 800;
    font-size: 36px;
    letter-spacing: 1px;
    color: var(--ink);
  }
  .holder {
    position: absolute;
    left: 44px;
    top: 108px;
  }
  .holder-name {
    font-weight: 700;
    font-size: 22px;
    color: var(--ink);
    letter-spacing: 0.5px;
  }
  .holder-role {
    font-weight: 700;
    font-size: 12px;
    color: var(--accent);
    letter-spacing: 0.5px;
    margin-top: 2px;
  }
  .brand-mark {
    position: absolute;
    right: 44px;
    top: 182px;
    display: flex;
    align-items: center;
    gap: 10px;
  }
  .brand-mark-dot {
    width: 14px;
    height: 14px;
    border-radius: 50%;
    background: var(--accent);
  }
  .brand-mark-name {
    font-weight: 800;
    font-size: 26px;
    letter-spacing: 1px;
    color: var(--accent);
  }
  .contact {
    position: absolute;
    left: 44px;
    bottom: 44px;
    list-style: none;
  }
  .contact li {
    display: flex;
    align-items: center;
    gap: 10px;
    font-size: 14px;
    color: var(--ink);
    margin-top: 6px;
  }
  .contact svg { width: 14px; height: 14px; }
</style>
</head>
<body>
<main class="stage">
  <section class="card card-front" aria-label="Business card front">
    <div class="world-map-area" role="img" aria-label="Dotted world map in dark grey"></div>
    <div class="front-wordmark">DEEP LOGIC</div>
  </section>

  <section class="card card-back" aria-label="Business card back">
    <div class="back-wordmark">DEEP LOGIC</div>

    <div class="holder">
      <div class="holder-name">DANIEL REED</div>
      <div class="holder-role">FOUNDER</div>
    </div>

    <div class="brand-mark">
      <span class="brand-mark-dot" aria-hidden="true"></span>
      <span class="brand-mark-name">DEEP LOGIC</span>
    </div>

    <ul class="contact">
      <li>
        <svg viewBox="0 0 16 16" aria-hidden="true">
          <path d="M3 2h3l1.5 3.5-2 1.2a8 8 0 0 0 3.8 3.8l1.2-2L14 10v3a1 1 0 0 1-1 1A11 11 0 0 1 2 3a1 1 0 0 1 1-1z" fill="var(--accent)"/>
        </svg>
        <span>000 000 0000</span>
      </li>
      <li>
        <svg viewBox="0 0 16 16" aria-hidden="true">
          <rect x="1" y="3" width="14" height="10" fill="var(--accent)"/>
          <path d="M1 3l7 6 7-6" fill="none" stroke="var(--white)" stroke-width="1.4"/>
        </svg>
        <span>info@danielreed.com</span>
      </li>
    </ul>
  </section>
</main>
</body>
</html>
```